PowerPoint Design Project for Korvath Bonding AB - a innovative adhesives company

We are looking to lift our current sales PPT template to convey a professional maturer image. Korvath Bonding AB (www.korvathbonding.example) develop a unique switchable adhesive that can be used in many different industries. Our strength in our technology is that the adhesive is stronger yet easier to remove in the same product.
We want to maintain our logo including its font (see attached).
We want to convey innovation, trustworthiness, Nordic (Sweden based) and high end (high tech) products.
Target Market(s)
Product managers, technical product owners, upper management, higher education levels.
Industry/Entity Type
It Company
Requirements
Must have
- 1) Existing logo
2) Index for presentation
3) Page numbers - or cool progress indicator indicating how much is left of the presentation
4) End slide - including contact details
5) Indicator of confidentiality
6) Headers, sub-headers, bullets synced (style)
Should not have
- Sounds and animations

```html
<!DOCTYPE html>
<html lang="en">
<head>
<meta charset="utf-8">
<title>Korvath Bonding AB – Presentation Template</title>
<link href="https://fonts.googleapis.com/css2?family=Arimo:wght@400;700&display=swap" rel="stylesheet">
<style>
  :root{
    --board:#dcdcdc;
    --paper:#ffffff;
    --brand:#1ba3d3;
    --brand-deep:#0b8fc0;
    --brand-light:#36c0ea;
    --ink:#2b2b2b;
    --text:#5a5a5a;
    --muted:#9a9a9a;
    --rule:#d8d8d8;
    --dot-off:#d9d9d9;
    --bar-grey:#8c8c8c;
    --card:#efefef;
  }
  *{box-sizing:border-box;margin:0;padding:0}
  html,body{width:1200px;height:900px;overflow:hidden;background:var(--board);font-family:"Arimo",Arial,sans-serif;color:var(--text)}
  .board{position:relative;width:1200px;height:900px}
  .slide{position:absolute;width:373px;height:280px;background:var(--paper);box-shadow:2px 3px 5px rgba(0,0,0,.28);overflow:hidden}
  .slide > *{position:absolute}

  .slide-title{left:23px;top:23px;font-size:15px;color:var(--brand);font-weight:400}
  .title-rule{left:21px;top:42px;width:330px;height:1px;background:linear-gradient(90deg,var(--brand),rgba(27,163,211,.15))}

  .progress{right:20px;top:3px;display:flex;gap:2px}
  .progress i{width:8px;height:8px;border-radius:50%;background:var(--dot-off);display:block}
  .progress i.on{background:var(--brand)}

  .footer-name{left:20px;bottom:8px;font-size:8px;font-weight:700;color:var(--ink);letter-spacing:.2px}
  .footer-copy{left:0;right:0;bottom:5px;text-align:center;font-size:4px;color:var(--muted)}
  .page-no{right:24px;bottom:4px;font-size:6px;color:var(--brand)}

  .bullets{list-style:none}
  .bullets li{position:relative;padding-left:7px}
  .bullets li::before{content:"";position:absolute;left:0;width:2px;height:2px;border-radius:50%;background:var(--brand)}

  /* brand card */
  .brand-card{width:206px;height:72px;background:var(--card);box-shadow:0 4px 5px rgba(0,0,0,.25);text-align:center}
  .brand-card .brand-name{display:block;margin-top:20px;font-size:21px;font-weight:700;color:var(--ink);letter-spacing:.5px}
  .brand-card .brand-web{display:block;margin-top:12px;font-size:4.5px;color:var(--muted);letter-spacing:.6px}

  /* title slide */
  .cover-title{left:0;right:0;top:196px;text-align:center;font-size:14.5px;font-weight:700;color:var(--brand)}
  .cover-sub{left:0;right:0;top:236px;text-align:center;font-size:7.5px;font-weight:700;color:var(--brand)}

  /* executive summary */
  .chevron{left:19px;width:68px;height:43px}
  .summary-text{left:96px;width:240px;font-size:5.4px;line-height:9px}
  .summary-text li::before{top:3.5px}

  /* agenda A */
  .agenda-heading{left:23px;top:55px;font-size:14px;font-weight:700;color:var(--ink)}
  .agenda-list{left:19px;top:80px;width:350px;font-size:7.5px;line-height:12px;list-style:none}
  .agenda-list li{display:flex;justify-content:space-between;padding:0 73px 0 10px;position:relative}
  .agenda-list li::before{content:"";position:absolute;left:4px;top:5px;width:2px;height:2px;border-radius:50%;background:var(--brand)}
  .agenda-list li.current{border:1px solid var(--brand);border-radius:2px;margin-left:-1px;width:336px}
  .agenda-list li.current span:last-child{margin-right:-73px;padding-right:73px}

  /* agenda B */
  .agenda-steps{left:19px;top:61px;width:334px;list-style:none;font-size:6.5px}
  .agenda-steps li{display:flex;align-items:center;height:34.3px;padding:0 50px 0 20px}
  .agenda-steps li.current{border:1px solid #b5b5b5;border-radius:2px;height:26px;margin:4px 0 4.3px}
  .step-no{width:12px;height:12px;border-radius:50%;background:var(--brand);color:#fff;font-weight:700;font-size:6px;display:flex;align-items:center;justify-content:center;margin-right:10px;box-shadow:0 1px 1px rgba(0,0,0,.3)}
  .step-label{flex:1}

  /* text slide */
  .body-text{left:23px;top:72px;width:330px;font-size:7.6px;line-height:9.6px}
  .body-text li{margin-bottom:5px}
  .body-text li::before{top:4px}

  /* chart slides */
  .chart{left:0;top:0}
  .chart text{font-family:"Arimo",Arial,sans-serif}
  .chart-notes{left:185px;top:98px;width:150px;font-size:5.8px;line-height:7.6px}
  .chart-notes li{margin-bottom:11px}
  .chart-notes li::before{top:3px}
  .callout{left:96px;top:100px;width:70px;height:34px;border-radius:4px;background:var(--brand);color:#fff;font-size:6.5px;line-height:8px;text-align:center;padding-top:9px;box-shadow:0 1px 2px rgba(0,0,0,.3)}
  .callout::after{content:"";position:absolute;left:42px;bottom:-6px;border:4px solid transparent;border-top:6px solid var(--brand);border-bottom:0}

  /* table */
  .data-table{left:32px;top:75px;width:310px;border-collapse:collapse;font-size:6px}
  .data-table th{background:var(--brand);color:#fff;text-align:left;font-weight:700;padding:3px 4px;height:14px}
  .data-table td{vertical-align:top;padding:5px 4px 8px;border-bottom:1px solid var(--rule)}
  .data-table td ul{line-height:8.6px}
  .data-table li::before{top:3.5px;background:var(--text)}

  /* closing */
  .thanks{left:0;right:0;top:181px;text-align:center;font-size:10px;font-weight:700;color:var(--brand)}
  .contact{left:0;right:0;top:220px;text-align:center;font-size:5px;line-height:14px;color:var(--text)}
</style>
</head>
<body>
<main class="board">

  <!-- 1 Cover -->
  <section class="slide" style="left:21px;top:15px">
    <div class="brand-card" style="left:81px;top:53px">
      <span class="brand-name">KORVATH BONDING</span>
      <span class="brand-web">www.korvathbonding.example</span>
    </div>
    <h1 class="cover-title">Insert The Title of Your Presentation Here</h1>
    <p class="cover-sub">Subtitle of the Presentation or main author’s name here</p>
    <p class="footer-copy">© 2013 Korvath Bonding AB. All Rights Reserved.</p>
  </section>

  <!-- 2 Executive summary -->
  <section class="slide" style="left:414px;top:15px">
    <h2 class="slide-title">Executive summary</h2>
    <div class="title-rule"></div>
    <svg class="chevron" style="top:75px" viewBox="0 0 68 43" aria-hidden="true">
      <defs><linearGradient id="chev" x1="0" y1="0" x2="0" y2="1"><stop offset="0" stop-color="#3cc6ee"/><stop offset="1" stop-color="#0b94c6"/></linearGradient></defs>
      <polygon points="0,0 56,0 68,21.5 56,43 0,43" fill="url(#chev)"/>
    </svg>
    <svg class="chevron" style="top:137px" viewBox="0 0 68 43" aria-hidden="true"><polygon points="0,0 56,0 68,21.5 56,43 0,43" fill="url(#chev)"/></svg>
    <svg class="chevron" style="top:199px" viewBox="0 0 68 43" aria-hidden="true"><polygon points="0,0 56,0 68,21.5 56,43 0,43" fill="url(#chev)"/></svg>
    <ul class="bullets summary-text" style="top:84px">
      <li>Lorem ipsum dolor sit amet, consectetur adipiscing elit.</li>
      <li>Duis blandit lorem eu libero congue aliquam vel sit amet augue.</li>
      <li>Mauris augue ipsum, dignissim vitae adipiscing eu, euismod nec sem.</li>
    </ul>
    <ul class="bullets summary-text" style="top:146px">
      <li>Lorem ipsum dolor sit amet, consectetur adipiscing elit.</li>
      <li>Duis blandit lorem eu libero congue aliquam vel sit amet augue.</li>
      <li>Mauris augue ipsum, dignissim vitae adipiscing eu, euismod nec sem.</li>
    </ul>
    <ul class="bullets summary-text" style="top:208px">
      <li>Lorem ipsum dolor sit amet, consectetur adipiscing elit.</li>
      <li>Duis blandit lorem eu libero congue aliquam vel sit amet augue.</li>
      <li>Mauris augue ipsum, dignissim vitae adipiscing eu, euismod nec sem.</li>
    </ul>
    <p class="footer-copy">© 2013 Korvath Bonding AB. All Rights Reserved.</p>
  </section>

  <!-- 3 Agenda (list) -->
  <section class="slide" style="left:807px;top:15px">
    <div class="progress"><i class="on"></i><i></i><i></i><i></i><i></i></div>
    <h2 class="agenda-heading">Agenda</h2>
    <ul class="agenda-list">
      <li class="current"><span>Introduction</span><span>09:00 – 09:15</span></li>
      <li><span>Subject 1</span><span>09:15 – 10:00</span></li>
      <li><span>Break</span><span>10:15 – 11:00</span></li>
      <li><span>Subject 2</span><span>11:00 – 11:45</span></li>
      <li><span>Closing &amp; Next steps</span><span>11:45 – 12:00</span></li>
    </ul>
    <p class="footer-name">KORVATH</p>
    <p class="footer-copy">© 2013 Korvath Bonding AB. All Rights Reserved.</p>
  </section>

  <!-- 4 Agenda (steps) -->
  <section class="slide" style="left:21px;top:310px">
    <div class="progress"><i class="on"></i><i></i><i></i><i></i><i></i></div>
    <h2 class="slide-title">Agenda</h2>
    <div class="title-rule"></div>
    <ol class="agenda-steps">
      <li class="current"><span class="step-no">1</span><span class="step-label">Introduction</span><span>09:00 – 09:15</span></li>
      <li><span class="step-no">2</span><span class="step-label">Subject 1</span><span>09:15 – 10:00</span></li>
      <li><span class="step-no">3</span><span class="step-label">Break</span><span>10:15 – 11:00</span></li>
      <li><span class="step-no">4</span><span class="step-label">Subject 2</span><span>11:00 – 11:45</span></li>
      <li><span class="step-no">5</span><span class="step-label">Closing &amp; Next steps</span><span>11:45 – 12:00</span></li>
    </ol>
    <p class="footer-copy">© 2013 Korvath Bonding AB. All Rights Reserved.</p>
    <p class="page-no">9</p>
  </section>

  <!-- 5 Text slide -->
  <section class="slide" style="left:414px;top:310px">
    <div class="progress"><i class="on"></i><i class="on"></i><i></i><i></i><i></i></div>
    <h2 class="slide-title">Text slide</h2>
    <div class="title-rule"></div>
    <ul class="bullets body-text">
      <li>Lorem ipsum dolor sit amet, consectetur adipiscing elit. Duis blandit lorem eu libero congue aliquam vel sit amet augue. Mauris augue ipsum, dignissim vitae adipiscing eu, euismod nec sem.</li>
      <li>Lorem ipsum dolor sit amet, consectetur adipiscing elit. Duis blandit lorem eu libero congue aliquam vel sit amet augue. Mauris augue ipsum, dignissim vitae adipiscing eu, euismod nec sem.</li>
      <li>Lorem ipsum dolor sit amet, consectetur adipiscing elit. Duis blandit lorem eu libero congue aliquam vel sit amet augue. Mauris augue ipsum, dignissim vitae adipiscing eu, euismod nec sem.</li>
      <li>Lorem ipsum dolor sit amet, consectetur adipiscing elit. Duis blandit lorem eu libero congue aliquam vel sit amet augue. Mauris augue ipsum, dignissim vitae adipiscing eu, euismod nec sem.</li>
    </ul>
    <p class="footer-name">KORVATH</p>
    <p class="footer-copy">© 2013 Korvath Bonding AB. All Rights Reserved.</p>
    <p class="page-no">10</p>
  </section>

  <!-- 6 Bar chart -->
  <section class="slide" style="left:807px;top:310px">
    <div class="progress"><i class="on"></i><i class="on"></i><i class="on"></i><i></i><i></i></div>
    <h2 class="slide-title">Graph Slide – Example 1</h2>
    <div class="title-rule"></div>
    <svg class="chart" width="373" height="280" viewBox="0 0 373 280" aria-label="Bar chart by quarter">
      <defs>
        <linearGradient id="barBlue" x1="0" y1="0" x2="0" y2="1"><stop offset="0" stop-color="#3cc6ee"/><stop offset="1" stop-color="#0b94c6"/></linearGradient>
        <linearGradient id="barGrey" x1="0" y1="0" x2="0" y2="1"><stop offset="0" stop-color="#a8a8a8"/><stop offset="1" stop-color="#777"/></linearGradient>
      </defs>
      <text x="105" y="84" font-size="6.5" font-weight="700" fill="#444" text-anchor="middle">Graph Title</text>
      <line x1="62" y1="94" x2="62" y2="230" stroke="#bbb" stroke-width=".6"/>
      <g font-size="5.5" fill="#444">
        <text x="56" y="111" text-anchor="end">1st Qtr</text>
        <text x="56" y="147" text-anchor="end">2nd Qtr</text>
        <text x="56" y="183" text-anchor="end">3rd Qtr</text>
        <text x="56" y="219" text-anchor="end">4th Qtr</text>
      </g>
      <rect x="62" y="99" width="93" height="19" fill="url(#barBlue)"/>
      <rect x="62" y="135" width="36" height="19" fill="url(#barGrey)"/>
      <rect x="62" y="171" width="16" height="19" fill="url(#barGrey)"/>
      <rect x="62" y="207" width="14" height="19" fill="url(#barGrey)"/>
      <g font-size="5.5" fill="#444">
        <text x="158" y="111">8,2</text>
        <text x="101" y="147">3,2</text>
        <text x="81" y="183">1,4</text>
        <text x="79" y="219">1,2</text>
      </g>
    </svg>
    <ul class="bullets chart-notes">
      <li>Lorem ipsum dolor sit amet, consectetur adipiscing elit. Duis blandit lorem eu libero congue aliquam vel sit amet augue. Mauris augue ipsum, dignissim vitae adipiscing eu, euismod nec sem.</li>
      <li>Lorem ipsum dolor sit amet, consectetur adipiscing elit. Duis blandit lorem eu libero congue aliquam vel sit amet augue. Mauris augue ipsum, dignissim vitae adipiscing eu, euismod nec sem.</li>
    </ul>
    <p class="footer-name">KORVATH</p>
    <p class="footer-copy">© 2013 Korvath Bonding AB. All Rights Reserved.</p>
    <p class="page-no">13</p>
  </section>

  <!-- 7 Line chart -->
  <section class="slide" style="left:21px;top:605px">
    <div class="progress"><i class="on"></i><i class="on"></i><i class="on"></i><i class="on"></i><i></i></div>
    <h2 class="slide-title">Graph Slide – Example 3</h2>
    <div class="title-rule"></div>
    <svg class="chart" width="373" height="280" viewBox="0 0 373 280" aria-label="Line chart by quarter">
      <text x="185" y="84" font-size="6.5" font-weight="700" fill="#444" text-anchor="middle">Graph Title</text>
      <line x1="51" y1="230" x2="351" y2="230" stroke="#bbb" stroke-width=".7"/>
      <polyline points="92,162 169,173 246,113 323,147" fill="none" stroke="#a8a8a8" stroke-width="1.4"/>
      <polyline points="92,211 169,207 246,180 323,102" fill="none" stroke="#1ba3d3" stroke-width="1.4"/>
      <g fill="#fff" stroke="#a8a8a8" stroke-width="1">
        <circle cx="92" cy="162" r="2.2"/><circle cx="169" cy="173" r="2.2"/><circle cx="246" cy="113" r="2.2"/><circle cx="323" cy="147" r="2.2"/>
      </g>
      <g fill="#fff" stroke="#1ba3d3" stroke-width="1">
        <circle cx="92" cy="211" r="2.2"/><circle cx="169" cy="207" r="2.2"/><circle cx="246" cy="180" r="2.2"/><circle cx="323" cy="102" r="2.2"/>
      </g>
      <g font-size="5.5" fill="#444" text-anchor="middle">
        <text x="92" y="155">4,4</text><text x="169" y="167">3,6</text><text x="246" y="106">7,5</text><text x="323" y="142">5,3</text>
        <text x="92" y="205">1,2</text><text x="169" y="201">1,4</text><text x="246" y="174">3,2</text><text x="323" y="96">8,2</text>
        <text x="92" y="240">1st Qtr</text><text x="169" y="240">2nd Qtr</text><text x="246" y="240">3rd Qtr</text><text x="323" y="240">4th Qtr</text>
      </g>
    </svg>
    <div class="callout">Key conclusion<br>added here...</div>
    <p class="footer-name">KORVATH</p>
    <p class="footer-copy">© 2013 Korvath Bonding AB. All Rights Reserved.</p>
    <p class="page-no">15</p>
  </section>

  <!-- 8 Table -->
  <section class="slide" style="left:414px;top:605px">
    <div class="progress"><i class="on"></i><i class="on"></i><i class="on"></i><i class="on"></i><i class="on"></i></div>
    <h2 class="slide-title">Sample Table 3x3</h2>
    <div class="title-rule"></div>
    <table class="data-table">
      <thead><tr><th>Title 1</th><th>Title 2</th><th>Title 3</th></tr></thead>
      <tbody>
        <tr>
          <td><ul class="bullets"><li>Ipsum lorum</li><li>Ipsum lorum</li><li>Ipsum lorum</li></ul></td>
          <td><ul class="bullets"><li>Ipsum lorum</li><li>Ipsum lorum</li><li>Ipsum lorum</li></ul></td>
          <td><ul class="bullets"><li>Ipsum lorum</li><li>Ipsum lorum</li><li>Ipsum lorum</li></ul></td>
        </tr>
        <tr>
          <td><ul class="bullets"><li>Ipsum lorum</li><li>Ipsum lorum</li><li>Ipsum lorum</li></ul></td>
          <td><ul class="bullets"><li>Ipsum lorum</li><li>Ipsum lorum</li><li>Ipsum lorum</li></ul></td>
          <td><ul class="bullets"><li>Ipsum lorum</li><li>Ipsum lorum</li><li>Ipsum lorum</li></ul></td>
        </tr>
        <tr>
          <td><ul class="bullets"><li>Ipsum lorum</li><li>Ipsum lorum</li><li>Ipsum lorum</li></ul></td>
          <td><ul class="bullets"><li>Ipsum lorum</li><li>Ipsum lorum</li><li>Ipsum lorum</li></ul></td>
          <td><ul class="bullets"><li>Ipsum lorum</li><li>Ipsum lorum</li><li>Ipsum lorum</li></ul></td>
        </tr>
      </tbody>
    </table>
    <p class="footer-name">KORVATH</p>
    <p class="footer-copy">© 2013 Korvath Bonding AB. All Rights Reserved.</p>
    <p class="page-no">17</p>
  </section>

  <!-- 9 Closing -->
  <section class="slide" style="left:807px;top:605px">
    <div class="brand-card" style="left:89px;top:81px">
      <span class="brand-name">KORVATH BONDING</span>
      <span class="brand-web">www.korvathbonding.example</span>
    </div>
    <h2 class="thanks">Thank You For Your Time!</h2>
    <p class="contact">
      KORVATH BONDING AB • Stensgatan 9 • 412 70 Göteborg, Sweden<br>
      Tel +46 700 481 263 • Fax +46 31 705 118<br>
      www.korvathbonding.example
    </p>
    <p class="footer-copy">© 2013 Korvath Bonding AB. All Rights Reserved.</p>
  </section>

</main>
</body>
</html>
```